Business Card for Mortuary

We need a business card design for our mortuary. We are not the "traditional" mortuary and specialize in simple cremations and burials. We use a two sided card.

Industry/Entity Type

Funeral Home

Contact Information for Business Card

One side we would like to have with the general information of the mortuary:
Address: 4172 E. Larkspur Ave, Alder Springs, CO 85904
Phone: 623-555-0148
email: hello@willowmereplace.com
website: willowmereplace.com

On the other side would like to have the information of employee:
Name: Peter K. Lund
Email: peter@willowmereplace.com
Title: Funeral Director
Text: 602-555-0173

Font styles to use
Serif
Sans Serif

Requirements
Should not have
• Do not put any gothic images or things like a hearse or tombstone.

```html
<!DOCTYPE html>
<html lang="en">
<head>
<meta charset="utf-8">
<title>Willowmere Place – Business Card</title>
<link href="https://fonts.googleapis.com/css2?family=Montserrat:wght@400;500;700&display=swap" rel="stylesheet">
<style>
  :root {
    --bg: #2b2b2b;
    --card-dark: #0b0b0b;
    --card-light: #ffffff;
    --green: #7cc242;
    --ink: #1c1c1c;
    --white: #ffffff;
  }
  * { box-sizing: border-box; margin: 0; padding: 0; }
  html, body { width: 1200px; height: 930px; overflow: hidden; }
  body {
    background: var(--bg);
    font-family: "Montserrat", Arial, sans-serif;
    display: flex;
    flex-direction: column;
    align-items: center;
    justify-content: center;
    gap: 46px;
  }
  .card {
    width: 680px;
    height: 389px;
    border-radius: 22px;
    position: relative;
    overflow: hidden;
    box-shadow: 0 14px 30px rgba(0,0,0,.45);
  }
  /* Back side */
  .card--back { background: var(--card-dark); }
  .card__pattern {
    position: absolute; inset: 0;
    background: radial-gradient(ellipse at 50% 50%, rgba(80,110,40,.28), rgba(40,60,20,.18) 60%, rgba(0,0,0,0) 100%);
  }
  .back__content {
    position: absolute; inset: 0;
    display: flex; flex-direction: column; align-items: center; justify-content: center;
    gap: 14px;
  }
  .brand-name {
    font-weight: 700;
    font-size: 38px;
    letter-spacing: 1px;
    color: var(--white);
    white-space: nowrap;
  }
  .slogan {
    color: var(--green);
    font-size: 18px;
    font-weight: 400;
    letter-spacing: 2px;
  }
  /* Front side */
  .card--front { background: var(--card-light); display: flex; }
  .front__brand {
    width: 47%;
    display: flex; flex-direction: column; justify-content: center;
    padding: 90px 0 0 34px;
  }
  .front__brand-row { display: flex; align-items: center; gap: 10px; }
  .front__mark {
    width: 22px; height: 22px; border-radius: 50%;
    background: var(--green);
    flex: none;
  }
  .front__brand .brand-name { color: var(--ink); font-size: 21px; letter-spacing: .5px; }
  .front__brand .slogan { font-size: 11px; letter-spacing: 1px; margin: 6px 0 0 32px; }
  .front__details {
    width: 53%;
    margin: 56px 0;
    border-left: 1.5px solid var(--green);
    padding: 10px 0 0 24px;
    color: var(--ink);
  }
  .person__name {
    color: var(--green);
    font-weight: 700;
    font-size: 26px;
    letter-spacing: .5px;
    text-transform: uppercase;
    line-height: 1;
  }
  .person__title { font-size: 15px; margin: 6px 0 8px 12px; }
  .contact { list-style: none; font-size: 14px; }
  .contact li { display: flex; align-items: center; gap: 8px; margin: 3px 0 3px 12px; white-space: nowrap; }
  .contact svg { width: 11px; height: 11px; flex: none; }
  .divider { height: 1.5px; background: var(--green); margin: 12px 20px 12px 12px; }
  .address { font-size: 14px; line-height: 1.35; margin-left: 12px; }
</style>
</head>
<body>
  <section class="card card--back" aria-label="Card back">
    <div class="card__pattern" role="img" aria-label="Repeating faint green leaf pattern on black"></div>
    <div class="back__content">
      <div class="brand-name">WILLOWMERE PLACE</div>
      <div class="slogan">Simple, Honest Farewells</div>
    </div>
  </section>

  <section class="card card--front" aria-label="Card front">
    <div class="front__brand">
      <div class="front__brand-row">
        <span class="front__mark"></span>
        <div class="brand-name">WILLOWMERE PLACE</div>
      </div>
      <div class="slogan">Simple, Honest Farewells</div>
    </div>
    <div class="front__details">
      <div class="person__name">Peter K. Lund</div>
      <div class="person__title">Funeral Director</div>
      <ul class="contact">
        <li><svg viewBox="0 0 12 12"><path d="M3 1l2 2.5-1.2 1.3a6 6 0 0 0 3.4 3.4L8.5 7 11 9l-1.5 2C5 10.5 1.5 7 1 2.5z" fill="var(--green)"/></svg>602-555-0173</li>
        <li><svg viewBox="0 0 12 12"><rect x="1" y="2.5" width="10" height="7" fill="none" stroke="var(--green)" stroke-width="1.3"/><path d="M1 2.5l5 4 5-4" fill="none" stroke="var(--green)" stroke-width="1.3"/></svg>peter@willowmereplace.com</li>
      </ul>
      <div class="divider"></div>
      <p class="address">4172 E. Larkspur Ave,<br>Alder Springs, CO 85904</p>
      <ul class="contact">
        <li><svg viewBox="0 0 12 12"><path d="M3 1l2 2.5-1.2 1.3a6 6 0 0 0 3.4 3.4L8.5 7 11 9l-1.5 2C5 10.5 1.5 7 1 2.5z" fill="var(--green)"/></svg>623-555-0148</li>
        <li><svg viewBox="0 0 12 12"><rect x="1" y="2.5" width="10" height="7" fill="none" stroke="var(--green)" stroke-width="1.3"/><path d="M1 2.5l5 4 5-4" fill="none" stroke="var(--green)" stroke-width="1.3"/></svg>hello@willowmereplace.com</li>
        <li><svg viewBox="0 0 12 12"><circle cx="6" cy="6" r="5" fill="none" stroke="var(--green)" stroke-width="1.2"/><path d="M1 6h10M6 1c-3 3-3 7 0 10M6 1c3 3 3 7 0 10" fill="none" stroke="var(--green)" stroke-width="1"/></svg>www.willowmereplace.com</li>
      </ul>
    </div>
  </section>
</body>
</html>
```